Postcard: Live Ever Kinder

Text for front: HOW TO CHANGE THE WORLD IN ONE [note: the word "one" should be underlined] STEPHint: It's up to you...[Note: add arrow or something to indicate "turn over"]Text for back: You're going to spend your entire life with someone you can never get away from. (Guess who?) Wouldn't you rather that person #LiveEverKinder than judgmental or critical? BE the change you want to see! Visit www.LiveEverKinder-hub.com for daily Bright Pebbles and community. PLEASE JOIN US![Note: add logo to left half of back side]Font preference for text: Josefin sans

Target Market(s)

People who would be attracted to Calvera church - unitarian universalist message. It's spiritual without being overtly religious, so the target market is probably early 30s and up but ideally won't turn off Millennials (folks under 30). It should attract attention of people who are open-minded and committed to progressive social change, tired of an atmosphere of hate-mongering and divisiveness.

Requirements
Nice to have
• It would be nice to convey a sense of challenge - there is an idea of "bright pebbles" so something related to fire/sparks is appropriate. This is meant to evoke a deeper, divine love more than a sense of romantic love. This love is more fierce than fluffy! Yet it calls us to be our best selves.
Should not have
• Please avoid excessive pink - just the logo is enough, as this design needs to appeal to men as well as women.

```html
<!DOCTYPE html>
<html lang="en">
<head>
<meta charset="utf-8">
<title>Live Ever Kinder – Postcard</title>
<link rel="stylesheet" href="https://fonts.googleapis.com/css2?family=Josefin+Sans:wght@300;400;600;700&family=Pinyon+Script&display=swap">
<style>
  :root {
    --backdrop: #262626;
    --paper: #ffffff;
    --ink: #2f2d2e;
    --pink: #e83e6f;
    --pink-soft: #f3a6c4;
    --panel-dark: #262224;
    --light-text: #ffffff;
  }
  * { margin: 0; padding: 0; box-sizing: border-box; }
  html, body {
    width: 900px; height: 1200px; overflow: hidden;
    background: var(--backdrop);
    font-family: "Josefin Sans", sans-serif;
  }
  .canvas { position: relative; width: 900px; height: 1200px; }

  /* ---------- Front ---------- */
  .card-front {
    position: absolute; left: 110px; top: 88px; width: 710px; height: 474px;
    background: var(--paper); overflow: hidden;
  }
  .brush-wash {
    position: absolute; left: 0; top: 0; width: 470px; height: 400px;
    background: linear-gradient(150deg, rgba(232,62,111,.55) 0%, rgba(243,166,196,.5) 35%, rgba(243,166,196,.15) 65%, rgba(255,255,255,0) 85%);
    clip-path: polygon(0 35%, 60% 0, 100% 0, 75% 45%, 35% 100%, 0 90%);
  }
  .title-frame {
    position: absolute; left: 35px; top: 34px; width: 623px; height: 238px;
    border: 1.5px solid var(--pink);
  }
  .headline {
    position: absolute; left: 0; width: 710px; text-align: center;
    color: var(--ink); line-height: 1; white-space: nowrap;
  }
  .headline--bold { top: 60px; font-size: 64px; font-weight: 600; letter-spacing: 1px; }
  .headline--light { font-size: 90px; font-weight: 300; letter-spacing: 1px; }
  .headline--row2 { top: 134px; }
  .headline--row3 { top: 222px; }
  .headline u { text-decoration-thickness: 3px; text-underline-offset: 10px; }
  .turn-arrow { position: absolute; left: 495px; top: 270px; }
  .hint {
    position: absolute; left: 0; top: 384px; width: 710px; text-align: center;
    font-family: "Pinyon Script", cursive; font-size: 38px; color: var(--ink); font-weight: 700;
  }
  .hint__label { color: var(--pink); font-size: 46px; }
  .divider {
    position: absolute; left: 45px; top: 438px; width: 620px; height: 1.5px; background: var(--ink);
  }

  /* ---------- Back ---------- */
  .card-back {
    position: absolute; left: 107px; top: 641px; width: 710px; height: 474px;
    background: var(--panel-dark); overflow: hidden;
  }
  .logo-panel {
    position: absolute; left: 0; top: 0; width: 355px; height: 339px; background: var(--paper);
    display: flex; align-items: center; justify-content: center; gap: 14px;
  }
  .logo-mark { width: 22px; height: 22px; border-radius: 50%; background: var(--pink); }
  .logo-name { font-size: 30px; font-weight: 400; color: var(--pink); letter-spacing: 1px; }
  .message {
    position: absolute; left: 371px; top: 36px; width: 323px;
    color: var(--light-text); font-size: 18px; line-height: 27px; text-align: justify;
  }
  .message p + p { margin-top: 26px; }
  .message strong { font-weight: 700; }
  .web-link {
    background: var(--pink); padding: 2px 8px 0; margin: 0 4px; font-size: 19px;
  }
  .join-band {
    position: absolute; left: 0; top: 339px; width: 710px; height: 103px;
    background: var(--pink); color: var(--light-text);
    font-size: 58px; font-weight: 300; text-align: center; line-height: 110px;
  }
  .test-note {
    position: absolute; left: 0; top: 442px; width: 355px; height: 32px;
    background: var(--paper); color: var(--ink); font-size: 13px; padding: 10px 0 0 14px;
  }
</style>
</head>
<body>
<main class="canvas">
  <section class="card-front">
    <div class="brush-wash" role="img" aria-label="Pink watercolour brush wash behind the headline"></div>
    <div class="title-frame"></div>
    <h1 class="headline headline--bold">HOW TO CHANGE</h1>
    <p class="headline headline--light headline--row2">THE WORLD</p>
    <p class="headline headline--light headline--row3">IN <u>ONE</u> STEP</p>
    <svg class="turn-arrow" width="215" height="110" viewBox="0 0 215 110" aria-hidden="true">
      <path d="M5 20 Q40 100 140 80 Q180 70 196 20 Q170 95 70 100 Q20 100 5 20 Z" fill="var(--pink)"/>
      <path d="M178 22 L215 8 L206 46 Z" fill="var(--pink)"/>
    </svg>
    <p class="hint"><span class="hint__label">Hint:</span> It's up to you...</p>
    <div class="divider"></div>
  </section>

  <section class="card-back">
    <div class="logo-panel">
      <span class="logo-mark"></span>
      <span class="logo-name">Live Ever Kinder</span>
    </div>
    <div class="message">
      <p>You're going to spend your entire life with someone you can never get away from. (Guess who?) Wouldn't you rather that person #LiveEverKinder than judgmental or critical?</p>
      <p><strong>BE</strong> the change you want to see! Visit <span class="web-link">www.LiveEverKinder-hub.com</span> for daily Bright Pebbles and community.</p>
    </div>
    <div class="join-band">PLEASE JOIN US!</div>
    <p class="test-note">A/B test:How to change/the world/your life</p>
  </section>
</main>
</body>
</html>
```